Bright Lanterns Business Card

Design of business cards

Target Market(s)

We are aiming as small business owners who need anything from basic business structures, website plans, business processes and quality assurance.

Industry/Entity Type

Business

Colors

Designer to choose colors to be used in the design.

Requirements
Nice to have
• I would prefer one side of the card to use the green from the logo. Prefer to have the same font as the logo.

```html
<!DOCTYPE html>
<html lang="en">
<head>
<meta charset="utf-8">
<title>Bright Lanterns Consulting – Business Cards</title>
<link href="https://fonts.googleapis.com/css2?family=Cinzel:wght@500&display=swap" rel="stylesheet">
<style>
  :root {
    --page: #ffffff;
    --deep-teal: #01302f;
    --mid-teal: #1b6261;
    --soft-teal: #659a97;
    --stripe-teal: #163f3d;
    --lime: #a6c93a;
    --ink: #000000;
    --back-black: #0b0b0b;
  }
  * { margin: 0; padding: 0; box-sizing: border-box; }
  html, body { width: 906px; height: 1200px; overflow: hidden; background: var(--page); }
  .canvas { position: relative; width: 906px; height: 1200px; }

  .card { position: absolute; left: 18px; width: 863px; overflow: hidden; }
  .card-front { top: 31px; height: 559px; background: var(--deep-teal); }
  .card-back { top: 614px; height: 560px; }

  .brand-band { position: absolute; left: 0; top: 74px; width: 467px; height: 163px; background: var(--mid-teal); }
  .texture { position: absolute; left: 467px; width: 295px; background: var(--stripe-teal); }
  .texture-top { top: 0; height: 237px; }
  .texture-bottom { top: 414px; height: 145px; }
  .contact-band { position: absolute; left: 0; top: 237px; width: 762px; height: 177px; background: var(--soft-teal); }

  .contact-icon { position: absolute; left: 31px; width: 46px; height: 46px; }
  .icon-mail { top: 6px; height: 30px; }
  .icon-info { top: 58px; }
  .icon-phone { top: 124px; }

  .wordmark { position: absolute; display: flex; align-items: center; gap: 18px; }
  .wordmark-dot { width: 70px; height: 70px; border-radius: 50%; background: var(--lime); flex: none; }
  .wordmark-name {
    font-family: "Cinzel", "Times New Roman", serif;
    font-weight: 500; font-size: 27px; line-height: 31px;
    letter-spacing: 1px; color: var(--lime);
  }
  .card-front .wordmark { left: 29px; top: 112px; }
  .card-back .wordmark { left: 127px; top: 230px; }

  .card-back svg { position: absolute; inset: 0; }
</style>
</head>
<body>
<main class="canvas">

  <section class="card card-front" aria-label="Business card front">
    <div class="brand-band"></div>
    <div class="texture texture-top" role="img" aria-label="Diagonal stripe texture"></div>
    <div class="texture texture-bottom" role="img" aria-label="Diagonal stripe texture"></div>

    <div class="wordmark">
      <span class="wordmark-dot"></span>
      <p class="wordmark-name">Bright<br>Lanterns<br>Consulting</p>
    </div>

    <div class="contact-band">
      <svg class="contact-icon icon-mail" viewBox="0 0 46 30" aria-label="Email">
        <rect x="1" y="1" width="44" height="28" fill="#fff" stroke="var(--ink)" stroke-width="2"/>
        <path d="M1 1 L23 18 L45 1 M1 29 L17 13 M45 29 L29 13" fill="none" stroke="var(--ink)" stroke-width="2"/>
      </svg>
      <svg class="contact-icon icon-info" viewBox="0 0 46 46" aria-label="Information">
        <circle cx="23" cy="23" r="22" fill="var(--ink)"/>
        <circle cx="23" cy="12" r="4" fill="#fff"/>
        <rect x="19.5" y="19" width="7" height="18" rx="2" fill="#fff"/>
      </svg>
      <svg class="contact-icon icon-phone" viewBox="0 0 46 46" aria-label="Phone">
        <path d="M8 2 L15 2 L19 13 L13 18 Q18 29 28 33 L33 27 L44 31 L44 38 Q42 45 34 44 Q10 39 2 12 Q2 4 8 2 Z" fill="var(--ink)"/>
      </svg>
    </div>
  </section>

  <section class="card card-back" aria-label="Business card back">
    <svg viewBox="0 0 863 560" preserveAspectRatio="none">
      <defs>
        <linearGradient id="bubble-tones" x1="0" y1="0" x2="0.3" y2="1">
          <stop offset="0" stop-color="#4a8cc0"/>
          <stop offset="0.25" stop-color="#4a3c9c"/>
          <stop offset="0.45" stop-color="#d657b0"/>
          <stop offset="0.65" stop-color="#3fb56e"/>
          <stop offset="0.85" stop-color="#d9a72a"/>
          <stop offset="1" stop-color="#4a2d8a"/>
        </linearGradient>
      </defs>
      <rect x="600" y="0" width="263" height="560" fill="url(#bubble-tones)" role="img" aria-label="Colourful overlapping bubbles"/>
      <path d="M0 0 L742 0 Q720 80 642 115 Q690 170 705 250 Q740 290 740 350 Q700 390 706 440 Q730 520 710 560 L0 560 Z"
            fill="var(--back-black)" role="img" aria-label="Black panel with faint stripe texture"/>
      <rect x="28" y="26" width="610" height="510" fill="none" stroke="#1d1d1d" stroke-width="1"/>
    </svg>
    <div class="wordmark">
      <span class="wordmark-dot"></span>
      <p class="wordmark-name">Bright<br>Lanterns<br>Consulting</p>
    </div>
  </section>

</main>
</body>
</html>
```